TRK MECHANICAL FRONT WINDOWS DESIGN

I have two windows 2320 length, 1870 depth.
I would like a logo on one window, like the logo on sign we had designed with possibly the gears behind like in sign.
Other window would like same colours as logo with details of business.
The background colour I would maybe like the same as sign but if you think something looks better then happy to see design.
Details on other window:
ALL MECHANICAL REPAIRS, SERVICING AND MAJOR OVERHAULS ON LIGHT, HEAVY VEHICLES, DRILL RIGS, COMPRESSORS AND BOOSTERS
CERTIFIED VEHICLE REPAIRER
0451937264
tandkmechanical52@mailvane.net
Maybe just details in some sort of design or have a picture of a 46 SERIES dune strider, Brenk truck or an engine

```html
<!DOCTYPE html>
<html lang="en">
<head>
<meta charset="utf-8">
<title>TRK Mechanical – Window Details</title>
<link rel="stylesheet" href="https://fonts.googleapis.com/css2?family=Exo+2:wght@700;800&display=swap">
<style>
  :root{
    --mesh-dark:#05070c;
    --gear-red:#7a0d10;
    --ribbon-deep:#0b2b5c;
    --ribbon-bright:#2677c4;
    --plate-grey:#3a3b3e;
    --plate-dark:#1e1f22;
    --edge-blue:#2f7ad6;
    --ink:#ffffff;
  }
  *{margin:0;padding:0;box-sizing:border-box}
  html,body{width:1200px;height:969px;overflow:hidden;background:var(--mesh-dark)}
  .window-panel{position:relative;width:1200px;height:969px;overflow:hidden;
    font-family:"Exo 2",sans-serif;color:var(--ink)}
  .artwork{position:absolute;inset:0;width:1200px;height:969px}
  .label{position:absolute;font-weight:800;letter-spacing:0.5px;white-space:nowrap;
    text-shadow:2px 3px 4px rgba(0,0,0,.7);line-height:1;transform:translate(-50%,-50%)}
  .label--headline{font-size:43px}
  .label--service{font-size:33px}
  .label--certified{font-size:34px}
  .brand{position:absolute;left:150px;top:762px;display:flex;align-items:center;gap:10px;transform:translateY(-50%)}
  .brand__dot{width:24px;height:24px;border-radius:50%;background:var(--gear-red)}
  .brand__name{font-size:36px;font-weight:800;color:var(--ink);line-height:1;white-space:nowrap}
  .contact{position:absolute;top:916px;font-size:31px;font-weight:800;line-height:1;transform:translateY(-50%);white-space:nowrap}
  .contact--phone{left:80px}
  .contact--email{left:392px}
</style>
</head>
<body>
<main class="window-panel">
  <svg class="artwork" viewBox="0 0 1200 969" xmlns="http://www.w3.org/2000/svg">
    <defs>
      <radialGradient id="meshGlow" cx="50%" cy="45%" r="70%">
        <stop offset="0" stop-color="#1a3457"/>
        <stop offset="1" stop-color="#070a12"/>
      </radialGradient>
      <linearGradient id="ribbonFill" x1="0" x2="1" y1="0" y2="0">
        <stop offset="0" stop-color="var(--ribbon-deep)"/>
        <stop offset="0.5" stop-color="var(--ribbon-bright)"/>
        <stop offset="1" stop-color="var(--ribbon-deep)"/>
      </linearGradient>
      <linearGradient id="plateFill" x1="0" x2="0" y1="0" y2="1">
        <stop offset="0" stop-color="var(--plate-grey)"/>
        <stop offset="1" stop-color="var(--plate-dark)"/>
      </linearGradient>
      <linearGradient id="truckFill" x1="0" x2="1" y1="0" y2="1">
        <stop offset="0" stop-color="#b3121a"/>
        <stop offset="0.55" stop-color="#5a0a0e"/>
        <stop offset="1" stop-color="#111"/>
      </linearGradient>
    </defs>

    <rect class="mesh-backdrop" width="1200" height="969" fill="url(#meshGlow)" role="img" aria-label="Dark blue hexagonal metal mesh texture"/>

    <circle class="gear gear--left" cx="-60" cy="245" r="215" fill="var(--gear-red)" role="img" aria-label="Red gear decoration"/>
    <circle class="gear gear--right" cx="1230" cy="425" r="140" fill="var(--gear-red)" role="img" aria-label="Red gear decoration"/>

    <g class="ribbon ribbon--top">
      <polygon points="223,174 258,120 300,174" fill="#222"/>
      <polygon points="960,174 925,120 883,174" fill="#222"/>
      <polygon points="240,75 945,75 905,160 282,160" fill="url(#ribbonFill)"/>
    </g>
    <g class="ribbon ribbon--second">
      <polygon points="1030,270 1108,312 1030,312" fill="#222"/>
      <polygon points="109,215 1100,215 1060,300 160,300" fill="url(#ribbonFill)"/>
    </g>

    <g class="plate" stroke="var(--edge-blue)" stroke-width="2" fill="url(#plateFill)">
      <polygon points="148,350 586,350 530,430 190,430"/>
      <polygon points="614,350 1055,350 1005,415 650,415"/>
      <polygon points="33,458 451,458 400,538 70,538"/>
      <polygon points="467,458 735,458 767,538 433,538"/>
      <polygon points="752,458 1166,458 1115,538 800,538"/>
    </g>

    <polygon class="ribbon ribbon--certified" points="47,569 667,569 630,653 47,653 92,611" fill="url(#ribbonFill)"/>

    <polygon class="vehicle-photo" points="776,540 1027,540 1200,600 1200,969 553,969 541,735 600,690 690,657 760,612" fill="url(#truckFill)" role="img" aria-label="Photo of a lifted red dual-cab ute with off-road tyres"/>

    <rect class="contact-band" x="0" y="890" width="1200" height="53" fill="url(#ribbonFill)" opacity="0.95"/>

    <g class="icon icon--phone" fill="none" stroke="#fff" stroke-width="2.5">
      <rect x="40" y="900" width="18" height="32" rx="3"/>
      <line x1="46" y1="927" x2="52" y2="927"/>
      <path d="M34 908 q-4 8 0 16 M64 908 q4 8 0 16"/>
    </g>
    <g class="icon icon--mail" fill="none" stroke="#fff" stroke-width="2.5">
      <rect x="336" y="903" width="40" height="27" rx="2"/>
      <polyline points="336,904 356,920 376,904"/>
    </g>
  </svg>

  <span class="label label--headline" style="left:592px;top:124px">ALL MECHANICAL REPAIRS</span>
  <span class="label label--headline" style="left:590px;top:263px">SERVICING AND MAJOR OVERHAULS ON</span>
  <span class="label label--service" style="left:370px;top:392px">LIGHT VEHICLES</span>
  <span class="label label--service" style="left:835px;top:392px">HEAVY VEHICLES</span>
  <span class="label label--service" style="left:243px;top:500px">COMPRESSORS</span>
  <span class="label label--service" style="left:600px;top:500px">DRILL RIGS</span>
  <span class="label label--service" style="left:960px;top:500px">BOOSTERS</span>
  <span class="label label--certified" style="left:363px;top:611px">CERTIFIED VEHICLE REPAIRER</span>

  <div class="brand">
    <span class="brand__dot"></span>
    <span class="brand__name">TRK MECHANICAL</span>
  </div>

  <span class="contact contact--phone">0451937264</span>
  <span class="contact contact--email">tandkmechanical52@mailvane.net</span>
</main>
</body>
</html>
```